BrivoLane Ute.

I want the full logo on one side. And the other side the card if right Ralf the logo the left half orange like the car in the logo color with Danielle R Morrow
Founder and CEO
Email symbol then dmorrow@brivolaneute.com
Www symbol. Then Brivolaneute.com
Phone symbol then 413-926-BRIV
The very bottom would like Brivo Lane Ute is a division of Harmond Vistas. LLC

```html
<!DOCTYPE html>
<html lang="en">
<head>
<meta charset="utf-8">
<title>Brivo Lane Ute — Business Card</title>
<link href="https://fonts.googleapis.com/css2?family=Montserrat:wght@300;400;600;700&display=swap" rel="stylesheet">
<style>
  :root {
    --stage: #e9e7e4;
    --card: #ffffff;
    --wine: #8b1c1c;
    --ink: #2a2a2a;
    --orange: #e8962e;
    --rule: #d9cfc6;
  }
  * { box-sizing: border-box; margin: 0; padding: 0; }
  html, body { width: 1200px; height: 900px; overflow: hidden; }
  body {
    background: var(--stage);
    font-family: "Montserrat", Arial, sans-serif;
    color: var(--ink);
    display: flex;
    flex-direction: column;
    align-items: center;
    justify-content: center;
    gap: 46px;
  }
  .card {
    position: relative;
    width: 660px;
    height: 377px;
    background: var(--card);
    box-shadow: 0 6px 18px rgba(0,0,0,.12);
  }
  .card-frame { position: absolute; inset: 0; width: 100%; height: 100%; }
  .card-frame path { fill: none; stroke: var(--wine); stroke-width: 1.4; }

  /* front */
  .card-front { display: flex; align-items: center; justify-content: center; }
  .brand { display: flex; align-items: center; gap: 14px; }
  .brand-mark { width: 22px; height: 22px; border-radius: 50%; background: var(--orange); }
  .brand-name {
    font-weight: 600;
    font-size: 40px;
    letter-spacing: 2px;
    text-transform: uppercase;
    color: var(--ink);
  }

  /* back */
  .card-back { display: flex; }
  .back-brand {
    width: 45%;
    display: flex;
    align-items: center;
    justify-content: center;
  }
  .back-brand .brand-name { font-size: 20px; letter-spacing: 1px; }
  .back-brand .brand-mark { width: 12px; height: 12px; }
  .divider {
    position: absolute;
    left: 45%;
    top: 80px;
    height: 120px;
    width: 1px;
    background: var(--rule);
  }
  .contact {
    padding: 72px 0 0 28px;
    flex: 1;
  }
  .person-name {
    font-size: 21px;
    color: var(--wine);
    text-transform: uppercase;
    letter-spacing: .3px;
  }
  .person-name .given { font-weight: 700; }
  .person-name .rest { font-weight: 300; }
  .person-title {
    font-size: 11px;
    text-transform: uppercase;
    letter-spacing: .5px;
    margin: 2px 0 12px;
  }
  .contact-list { list-style: none; }
  .contact-list li {
    display: flex;
    align-items: center;
    gap: 10px;
    font-size: 12.5px;
    margin-bottom: 6px;
  }
  .contact-list svg { width: 12px; height: 12px; fill: none; stroke: var(--wine); stroke-width: 1.6; }
  .contact-list svg .solid { fill: var(--wine); stroke: none; }
  .division-note {
    position: absolute;
    left: 0; right: 0;
    bottom: 40px;
    text-align: center;
    font-size: 12px;
    color: var(--wine);
  }
</style>
</head>
<body>

<section class="card card-front">
  <svg class="card-frame" viewBox="0 0 660 377" aria-hidden="true">
    <path d="M32 18 H628 A14 14 0 0 0 642 32 V345 A14 14 0 0 0 628 359 H32 A14 14 0 0 0 18 345 V32 A14 14 0 0 0 32 18 Z"/>
  </svg>
  <div class="brand">
    <span class="brand-mark"></span>
    <span class="brand-name">Brivo Lane Ute</span>
  </div>
</section>

<section class="card card-back">
  <svg class="card-frame" viewBox="0 0 660 377" aria-hidden="true">
    <path d="M32 18 H628 A14 14 0 0 0 642 32 V345 A14 14 0 0 0 628 359 H32 A14 14 0 0 0 18 345 V32 A14 14 0 0 0 32 18 Z"/>
  </svg>
  <div class="back-brand">
    <div class="brand">
      <span class="brand-mark"></span>
      <span class="brand-name">Brivo Lane Ute</span>
    </div>
  </div>
  <span class="divider"></span>
  <div class="contact">
    <h1 class="person-name"><span class="given">Danielle</span> <span class="rest">R Morrow</span></h1>
    <p class="person-title">Founder and CEO</p>
    <ul class="contact-list">
      <li>
        <svg viewBox="0 0 12 12"><rect x="3" y="1" width="6" height="10" rx="1"/></svg>
        413-926-BRIV
      </li>
      <li>
        <svg viewBox="0 0 12 12"><rect class="solid" x="1" y="3" width="10" height="7"/><path d="M1 3 L6 7 L11 3" stroke="#fff"/></svg>
        dmorrow@brivolaneute.com
      </li>
      <li>
        <svg viewBox="0 0 12 12"><circle cx="6" cy="6" r="5"/><ellipse cx="6" cy="6" rx="2" ry="5"/><path d="M1 6 H11"/></svg>
        www.brivolaneute.com
      </li>
    </ul>
  </div>
  <p class="division-note">Brivo Lane Ute is a division of Harmond Vistas. LLC</p>
</section>

</body>
</html>
```